www.brevatin.com Sales/Order Page ReDesign

We need a new and amazing design for our sales/order page to attract more costumers and new houses for our portal.

Here is the existing page with the current design: https://www.brevatin.com/sales

We are proud owners of www.sommarhytta.no and www.brevatin.com and we want more holiday home owners to join our page so that we can rent out their holiday homes and increase the number of houses on our portal.

To get more homeowners we need a sales page that can sell our products the best way possible. Therefore we want you too blow us away with a fresh, modern, easy understandable and stylish new sales/order page.

The only restrictions we give when it comes to design is that it needs to fit the existing design of our portals, the top and footer are set. Beside that we are open for everything as long as it at once give the customers impression that this is a good, professional page were they just have to put out their houses.

When it comes to content I have added two documents who include the content to put in here and some guidelines on how to organize the page. Please be creative and add necessary graphics, symbols, background pictures and what ever necessary to make this page look professional and appealing to new costumers.

Looking forward to what suggestions we are given.

We just want to inform that we have updated our brief with a much more concrete description of what content to add on the sale page, and who to structure the content on the page. Hope this helps to make suggestions easier. Looking forward to receive some good contributions.

We would just like to make sure that everyone have understood that we are not asking for a new design suggestion to our portal in general. We are only asking for a redesign of our sales/order page you find here www.brevatin.com/sales. We have to day received some designs for our front page and the design it self was good, but that's not what we are asking for this time and don't want you to use time of something we don't need at the moment. We are looking forward too se some good suggestions.

Reason: Hello. Thanks for all the great contributions we have been given so fare. We haven't been able to respond to all design and are therefore extending the deadline so that we are able to respond to the designs we have been giver and to gov time to make final changes.

Reason: We are extending the deadline to give designers time to give new suggestion based on our latest feedback today.

Reason: Extended so we can receive last design changes.

Target Market(s)

This is a presentation page where we present our product agains new home owner who we what to choose listing there property on or site.

Industry/Entity Type

Sales

Requirements
Must have
• A modern design who calms the costumer down and help them in deciding to chose us, and for them to choose us they need to trust and believe in us. Therefore your main task is to create a page that effectively informs about our product, gets the visitors attentions and make them trust us.
Nice to have
• Examples of good competitors and good order pages we like:

http://www.cabinquest.example/info/lyp?icid=IL___O_Text___top_nav_link
https://www.nestlodge.example/rooms/new
https://www.pearvix.example/phone/compare/
http://www.guestnook.example/host
Should not have
• - Bad design :-). With bad design we mean design that looks like it's made in 2 seconds by a little child.

```html
<!DOCTYPE html>
<html lang="en">
<head>
<meta charset="utf-8">
<title>Brevatin – List your property</title>
<link rel="stylesheet" href="https://fonts.googleapis.com/css2?family=Open+Sans:wght@400;600;700&display=swap">
<style>
:root{
  --blue:#1a8ee4;
  --blue-dark:#0f74c4;
  --footer-top:#1f95e6;
  --footer-bottom:#0a6fc0;
  --green-top:#c6ea6a;
  --green-bottom:#93c93a;
  --green-border:#7fae2c;
  --text:#222;
  --muted:#666;
  --field:#8c8c8c;
  --grey-band:#6f6e6c;
  --white:#fff;
}
*{box-sizing:border-box;margin:0;padding:0}
html,body{width:1200px;height:2395px;overflow:hidden}
body{position:relative;background:var(--white);font-family:"Open Sans",Arial,sans-serif;color:var(--text)}
.card{position:absolute;left:90px;top:12px;width:1052px;height:1572px;background:var(--white);box-shadow:0 0 10px rgba(0,0,0,.18)}
.card-title{position:absolute;left:0;top:8px;width:100%;height:53px;background:var(--blue);color:var(--white);font-weight:700;font-size:27px;letter-spacing:.5px;text-align:center;line-height:53px}
.intro{position:absolute;top:81px;left:25px;width:1000px;display:flex}
.intro-col{width:500px}
.intro-col h2{font-size:18px;font-weight:700;line-height:23px;color:#111}
.intro-col p{margin-top:18px;font-size:15px;line-height:21px;color:var(--muted)}
.intro-col.left{padding-right:30px;border-right:1px solid #bbb;height:140px}
.intro-col.right{padding-left:34px}
.rule{position:absolute;left:25px;width:1000px;height:2px;background:#999}
.lead-form{position:absolute;left:25px;top:268px;width:634px;display:grid;grid-template-columns:308px 308px;column-gap:18px}
.field label{display:block;font-size:14px;color:var(--muted);height:26px;line-height:22px}
.field input{display:block;width:308px;height:34px;border:1px solid var(--field);margin-bottom:20px;background:var(--white)}
.btn-green{background:linear-gradient(var(--green-top),var(--green-bottom));border:1px solid var(--green-border);color:#2c3a0c;font-family:inherit;text-align:center}
.lead-form .btn-green{grid-column:1 / span 2;height:42px;font-size:17px;margin-top:-4px;line-height:40px}
.advisor{position:absolute;left:790px;top:245px;width:150px;height:170px;border-radius:8px;background:linear-gradient(#dfe9f4,#bcd3ea)}
.advisor-note{position:absolute;left:712px;top:445px;width:310px;text-align:center;font-size:15px;line-height:24px;color:#333}
.plans{position:absolute;left:0;top:589px;width:1052px;display:flex;gap:17px}
.plan{width:339px;position:relative;height:796px}
.plan:first-child{width:350px}
.plan-head{height:66px;background:var(--blue);color:var(--white);padding:8px 12px;display:flex;justify-content:space-between}
.plan-head .price{font-size:21px;font-weight:700;line-height:24px}
.plan-head .unit{font-size:14px;line-height:22px}
.plan-head .rate{text-align:right;font-size:21px;font-weight:700;line-height:24px;width:70px}
.plan-head .rate span{display:block;text-align:left;font-size:14px;font-weight:400;line-height:22px}
.plan-fee{display:flex;gap:10px;margin:20px 0 0 12px;font-size:14px;line-height:18px;color:#333}
.plan-features{list-style:none;margin:26px 0 0 22px}
.plan-features li{display:flex;gap:14px;font-size:15px;line-height:19px;margin-bottom:14px;width:240px}
.plan-features svg{flex:none;margin-top:4px}
.partner{display:flex;align-items:center;gap:10px;margin-left:30px;font-weight:700;color:var(--blue-dark)}
.partner i{display:block;background:var(--blue-dark)}
.partner.main{font-size:36px;margin-top:12px;height:56px}
.partner.main i{width:38px;height:38px}
.partner.second{font-size:26px;margin-top:8px;height:40px}
.partner.second i{width:26px;height:26px}
.partner.third{font-size:30px;margin-top:16px;height:54px}
.partner.third i{width:44px;height:44px;border-radius:50%}
.upgrade{margin:20px 0 0 68px;font-size:15px;line-height:28px}
.upgrade h3{font-size:15px;font-weight:700;margin-bottom:4px}
.upgrade td:first-child{width:112px}
.plan .btn-green{position:absolute;left:25px;top:792px;width:242px;height:40px;font-size:15px;line-height:38px;border-radius:3px}
.help{position:absolute;left:25px;top:1485px;width:1000px;display:flex;justify-content:space-between;align-items:center}
.help p{font-size:15px;line-height:21px;width:620px}
.help a{color:var(--blue-dark);text-decoration:none}
.btn-blue{width:358px;height:45px;background:var(--blue);color:var(--white);font-size:17px;letter-spacing:.5px;line-height:45px;text-align:center}
.callback{position:absolute;left:0;top:1606px;width:1200px;height:462px;background:var(--grey-band);color:var(--white)}
.callback h2{position:absolute;top:30px;left:0;width:100%;text-align:center;font-size:19px;line-height:25px;font-weight:700}
.callback-form{position:absolute;left:93px;top:128px;display:grid;grid-template-columns:310px 310px;column-gap:38px}
.callback-form label{display:block;font-size:14px;line-height:20px;height:20px}
.callback-form input,.callback-form textarea{display:block;width:310px;height:33px;border:none;background:var(--white);margin-bottom:25px}
.callback-form textarea{height:82px;resize:none}
.callback-form .btn-green{height:38px;font-size:16px;line-height:36px;color:#2c3a0c;margin-top:-8px}
.office{position:absolute;left:826px;top:148px;font-size:14px;line-height:21px;font-style:normal}
.office dl{margin-top:24px;display:grid;grid-template-columns:78px auto;line-height:25px}
.site-footer{position:absolute;left:0;top:2073px;width:1200px;height:322px;background:linear-gradient(var(--footer-top),var(--footer-bottom));color:var(--white);font-size:14px}
.foot-col{position:absolute;top:50px}
.foot-col h3{font-size:15px;font-weight:700;margin-bottom:8px}
.foot-col ul{list-style:none;line-height:25px}
.foot-col li{display:flex;align-items:center;gap:10px}
.foot-col li i{width:13px;height:13px;border-radius:50%;background:var(--white);flex:none}
.foot-sep{position:absolute;top:20px;width:1px;height:140px;background:rgba(255,255,255,.35)}
.world-map{position:absolute;left:255px;top:35px;width:222px;height:150px;background:linear-gradient(rgba(255,255,255,.35),rgba(255,255,255,.15));border-radius:40%}
.contact li svg{flex:none}
</style>
</head>
<body>

<main class="card">
  <h1 class="card-title">HOW DO YOU WANT TO LIST YOUR PROPERTY?</h1>

  <section class="intro">
    <div class="intro-col left">
      <h2>Save time while we create income on your property Let our professional team handle your inquiries</h2>
      <p>Let our professional team handle your inquiries and bookings, and just sit and wait for the custumer to arrive at your property knowing you will get paid.</p>
    </div>
    <div class="intro-col right">
      <h2>Do it yourself</h2>
      <p style="margin-top:40px">Handle inquiries and bookings yourself, with help with our advance tools</p>
    </div>
  </section>

  <div class="rule" style="top:230px"></div>

  <form class="lead-form">
    <div class="field"><label>First Name</label><input type="text"></div>
    <div class="field"><label>Last Name</label><input type="text"></div>
    <div class="field"><label>E-mail</label><input type="text"></div>
    <div class="field"><label>Phone Number</label><input type="text"></div>
    <div class="field"><label>How they want to be contacted</label><input type="text"></div>
    <div class="field"><label>When they want to be contacted</label><input type="text"></div>
    <div class="btn-green">SUBMIT</div>
  </form>

  <div class="advisor" role="img" aria-label="Illustration of a friendly advisor holding a phone and giving a thumbs up"></div>
  <p class="advisor-note">We want to contact you to find the best way managing your portfolio of properties type in your contact details and we will contact you as soon as possible</p>

  <section class="plans">
    <article class="plan">
      <header class="plan-head"><div><div class="price">€ 995</div><div class="unit">Annually Booking</div></div><div class="rate">0%<span>Per</span></div></header>
      <div class="plan-fee"><svg width="18" height="18" viewBox="0 0 24 24"><path d="M12 2l3 7 7 .6-5.4 4.7 1.7 7.2L12 17.8 5.7 21.5l1.7-7.2L2 9.6 9 9z" fill="none" stroke="#333" stroke-width="2"/></svg><span>Transaction fee for secure payment<br>4,5% comes in addition</span></div>
      <ul class="plan-features">
        <li><svg width="8" height="12" viewBox="0 0 8 12"><path d="M1 1l5 5-5 5" fill="none" stroke="#111" stroke-width="2.4"/></svg>Our professional team is there for you</li>
        <li><svg width="8" height="12" viewBox="0 0 8 12"><path d="M1 1l5 5-5 5" fill="none" stroke="#111" stroke-width="2.4"/></svg>One upfront fee</li>
        <li><svg width="8" height="12" viewBox="0 0 8 12"><path d="M1 1l5 5-5 5" fill="none" stroke="#111" stroke-width="2.4"/></svg>No limits or fee on bookings.</li>
        <li><svg width="8" height="12" viewBox="0 0 8 12"><path d="M1 1l5 5-5 5" fill="none" stroke="#111" stroke-width="2.4"/></svg>No limits or fee on bookings request</li>
        <li><svg width="8" height="12" viewBox="0 0 8 12"><path d="M1 1l5 5-5 5" fill="none" stroke="#111" stroke-width="2.4"/></svg>Advertise your property for 12 months</li>
        <li><svg width="8" height="12" viewBox="0 0 8 12"><path d="M1 1l5 5-5 5" fill="none" stroke="#111" stroke-width="2.4"/></svg>Include announcements on:</li>
      </ul>
      <div class="partner main"><i></i>Brevatin</div>
      <div class="partner second"><i></i>Sommarhytta.no</div>
      <div class="partner third"><i></i>Tunvik</div>
      <div class="btn-green">Choose A New House</div>
    </article>

    <article class="plan">
      <header class="plan-head"><div><div class="price">€ 0</div><div class="unit">Annually Booking</div></div><div class="rate">18%<span>Per</span></div></header>
      <div class="plan-fee"><svg width="18" height="18" viewBox="0 0 24 24"><path d="M12 2l3 7 7 .6-5.4 4.7 1.7 7.2L12 17.8 5.7 21.5l1.7-7.2L2 9.6 9 9z" fill="none" stroke="#333" stroke-width="2"/></svg><span>Transaction fee for secure payment<br>4,5% comes in addition</span></div>
      <ul class="plan-features">
        <li><svg width="8" height="12" viewBox="0 0 8 12"><path d="M1 1l5 5-5 5" fill="none" stroke="#111" stroke-width="2.4"/></svg>Our professional team is there for you</li>
        <li><svg width="8" height="12" viewBox="0 0 8 12"><path d="M1 1l5 5-5 5" fill="none" stroke="#111" stroke-width="2.4"/></svg>No listing fee</li>
        <li><svg width="8" height="12" viewBox="0 0 8 12"><path d="M1 1l5 5-5 5" fill="none" stroke="#111" stroke-width="2.4"/></svg>No limits on bookings.</li>
        <li><svg width="8" height="12" viewBox="0 0 8 12"><path d="M1 1l5 5-5 5" fill="none" stroke="#111" stroke-width="2.4"/></svg>No limits or fee on bookings request</li>
        <li><svg width="8" height="12" viewBox="0 0 8 12"><path d="M1 1l5 5-5 5" fill="none" stroke="#111" stroke-width="2.4"/></svg>You decide when to advertise and for how long</li>
        <li><svg width="8" height="12" viewBox="0 0 8 12"><path d="M1 1l5 5-5 5" fill="none" stroke="#111" stroke-width="2.4"/></svg>Include announcements on:</li>
      </ul>
      <div class="partner main"><i></i>Brevatin</div>
      <div class="partner second"><i></i>Sommarhytta.no</div>
      <div class="upgrade"><h3>Upgrade with Tunvik.no:</h3>
        <table><tr><td>60 days</td><td>€ 50</td></tr><tr><td>120 days</td><td>€ 90</td></tr><tr><td>240 days</td><td>€ 160</td></tr><tr><td>1 year</td><td>€ 240</td></tr></table></div>
      <div class="btn-green">Choose A New House</div>
    </article>

    <article class="plan">
      <header class="plan-head"><div><div class="price">€ 0</div><div class="unit">Annually Booking</div></div><div class="rate">2%<span>Per</span></div></header>
      <div class="plan-fee"><svg width="18" height="18" viewBox="0 0 24 24"><path d="M12 2l3 7 7 .6-5.4 4.7 1.7 7.2L12 17.8 5.7 21.5l1.7-7.2L2 9.6 9 9z" fill="none" stroke="#333" stroke-width="2"/></svg><span>Transaction fee for secure payment<br>4,5% comes in addition</span></div>
      <ul class="plan-features">
        <li><svg width="8" height="12" viewBox="0 0 8 12"><path d="M1 1l5 5-5 5" fill="none" stroke="#111" stroke-width="2.4"/></svg>You handle everything yourself</li>
        <li><svg width="8" height="12" viewBox="0 0 8 12"><path d="M1 1l5 5-5 5" fill="none" stroke="#111" stroke-width="2.4"/></svg>No listing fee</li>
        <li><svg width="8" height="12" viewBox="0 0 8 12"><path d="M1 1l5 5-5 5" fill="none" stroke="#111" stroke-width="2.4"/></svg>No limits on bookings.</li>
        <li><svg width="8" height="12" viewBox="0 0 8 12"><path d="M1 1l5 5-5 5" fill="none" stroke="#111" stroke-width="2.4"/></svg>No limits or fee on bookings request</li>
        <li><svg width="8" height="12" viewBox="0 0 8 12"><path d="M1 1l5 5-5 5" fill="none" stroke="#111" stroke-width="2.4"/></svg>You decide when to advertise and for how long</li>
        <li><svg width="8" height="12" viewBox="0 0 8 12"><path d="M1 1l5 5-5 5" fill="none" stroke="#111" stroke-width="2.4"/></svg>Include announcements on:</li>
      </ul>
      <div class="partner main"><i></i>Brevatin</div>
      <div class="partner second"><i></i>Sommarhytta.no</div>
      <div class="upgrade"><h3>Upgrade with Tunvik.no:</h3>
        <table><tr><td>60 days</td><td>€ 50</td></tr><tr><td>120 days</td><td>€ 90</td></tr><tr><td>240 days</td><td>€ 160</td></tr><tr><td>1 year</td><td>€ 240</td></tr></table></div>
      <div class="btn-green">Choose A New House</div>
    </article>
  </section>

  <div class="rule" style="top:1460px"></div>

  <section class="help">
    <p>You now know that you are going to list your property, but are uncertain which listing option is right for you? <a href="#">Click here</a> to calculate what's most profitable for you...</p>
    <div class="btn-blue">BOOKING COMPARISON CALCULATOR</div>
  </section>
</main>

<section class="callback">
  <h2>If you want personal guidelines we are more then willing to call you, type in your name and number here<br>and someone will contact you as soon as possible</h2>
  <form class="callback-form">
    <div><label>First Name *</label><input type="text"></div>
    <div><label>Last Name *</label><input type="text"></div>
    <div><label>E-mail &nbsp;* (never shared)</label><input type="text"></div>
    <div><label>Phone Number * (never shared)</label><input type="text"></div>
    <div><label>Address</label><textarea></textarea></div>
    <div><label>When they want to be contacted</label><input type="text"><div class="btn-green">SUBMIT</div></div>
  </form>
  <address class="office">
    To<br>Brevatin Holiday Rental<br>Postboks 71 Lindeveien<br>5120 BERGEN<br>Norway
    <dl><dt style="grid-column:1 / span 2">Customer Service Center</dt>
      <dt>Phone</dt><dd>+47 55 40 21 87</dd>
      <dt>E-mail</dt><dd>post@brevatin.com</dd>
      <dt>website</dt><dd>www.brevatin.com</dd></dl>
  </address>
</section>

<footer class="site-footer">
  <div class="foot-col" style="left:93px"><h3>Destinations</h3>
    <ul><li><i></i>Europe</li><li><i></i>North America</li><li><i></i>South America</li><li><i></i>Africa</li><li><i></i>Asia</li><li><i></i>Australia</li></ul></div>
  <div class="world-map" role="img" aria-label="World map showing the rental destinations"></div>
  <div class="foot-sep" style="left:490px"></div>
  <div class="foot-col" style="left:508px"><h3>For tenants</h3>
    <ul><li><i></i>My page</li><li><i></i>Why Brevatin?</li><li><i></i>Help</li><li><i></i>Rental terms</li></ul></div>
  <div class="foot-sep" style="left:672px"></div>
  <div class="foot-col" style="left:692px"><h3>For house owners</h3>
    <ul><li><i></i>MyAdmin</li><li><i></i>Let us rent your house</li><li><i></i>Conditions</li></ul></div>
  <div class="foot-sep" style="left:912px"></div>
  <div class="foot-col contact" style="left:932px;top:40px"><h3 style="margin-bottom:2px">Contact us</h3>
    <ul style="line-height:23px">
      <li style="padding-left:23px">Brevatin Holiday Rental</li>
      <li><svg width="13" height="11" viewBox="0 0 13 11"><rect x=".5" y=".5" width="12" height="10" fill="none" stroke="#fff"/><path d="M.5 .5l6 5 6-5" fill="none" stroke="#fff"/></svg>post@brevatin.com</li>
      <li><svg width="13" height="13" viewBox="0 0 24 24"><path d="M6 2l4 4-2 3c1 3 4 6 7 7l3-2 4 4-3 4C10 22 2 14 2 5z" fill="#fff"/></svg>+47 55 40 21 87</li>
      <li><svg width="13" height="13" viewBox="0 0 14 14"><circle cx="7" cy="7" r="6" fill="none" stroke="#fff"/><path d="M1 7h12M7 1c-3 3-3 9 0 12M7 1c3 3 3 9 0 12" fill="none" stroke="#fff"/></svg>www.brevatin.com</li>
    </ul>
    <h3 style="margin:6px 0 2px">Opening hours</h3>
    <ul style="line-height:23px">
      <li><svg width="13" height="13" viewBox="0 0 14 14"><circle cx="7" cy="7" r="6" fill="none" stroke="#fff"/><path d="M7 3v4h3" fill="none" stroke="#fff"/></svg>Mon - Fri: 9.00 AM - 5.00 PM</li>
      <li><svg width="13" height="13" viewBox="0 0 14 14"><circle cx="7" cy="7" r="6" fill="none" stroke="#fff"/><path d="M7 3v4h3" fill="none" stroke="#fff"/></svg>Sat - Sun: Closed</li>
    </ul></div>
</footer>

</body>
</html>
```